Borvel Stake Pool, redesign of existing website

Borvel is a stake pool that allow its users to stake their Marevo crypto to yearn stable yields. The existing site is at www.borvelstake.org The site is today is a little dull and I want to have suggestions for a redesign that makes the site stand out and that picks up the colors of the logo. I am not looking for a complete redesign, mainly colors and smaller changes to layout. Examples of sites to be inspired by www.quenda.network, https://app.tervalo.finance/

Target Market(s)

Crypto users on Marevo

Number of Pages Required

1 page

```html
<!DOCTYPE html>
<html lang="en">
<head>
<meta charset="utf-8">
<title>Borvel Stake — Liquid Staking on Marevo</title>
<link rel="stylesheet" href="https://fonts.googleapis.com/css2?family=Bree+Serif&family=Inter:wght@400;500&display=swap">
<style>
  :root {
    --ink: #14201b;
    --text: #1f2a26;
    --muted: #8a9a96;
    --teal: #14a89c;
    --teal-dark: #0f8f85;
    --check: #3ccf8e;
    --mint: #c4f0cf;
    --lime: #e6f7c0;
    --sky: #9fe6ef;
    --white: #ffffff;
    --token: #1b1f2a;
  }
  * { box-sizing: border-box; margin: 0; padding: 0; }
  html, body { width: 1200px; height: 668px; overflow: hidden; }
  body {
    position: relative;
    font-family: "Inter", sans-serif;
    color: var(--text);
    background:
      radial-gradient(ellipse 420px 300px at 1210px 520px, rgba(130,220,238,.85), transparent 70%),
      radial-gradient(ellipse 520px 260px at 1100px 60px, rgba(226,247,184,.95), transparent 70%),
      radial-gradient(ellipse 620px 360px at 640px 40px, rgba(176,236,190,.95), transparent 70%),
      radial-gradient(ellipse 500px 300px at 120px 40px, rgba(200,240,215,.6), transparent 70%),
      var(--white);
  }
  .abs { position: absolute; }

  /* header */
  .site-header { position: absolute; left: 0; top: 0; width: 1200px; height: 66px;
    background: rgba(255,255,255,.15); box-shadow: 0 4px 14px rgba(80,140,100,.06); }
  .brand { left: 53px; top: 21px; display: flex; align-items: center; gap: 10px;
    font-family: "Bree Serif", serif; font-size: 15px; color: var(--ink); }
  .brand-dot { width: 20px; height: 20px; border-radius: 50%; background: var(--teal); }
  .nav-link { top: 18px; height: 32px; line-height: 32px; font-size: 13px; color: var(--ink); text-align: center; }
  .nav-link.is-active { background: rgba(255,255,255,.25); border-radius: 8px; }
  .wallet-select { left: 927px; top: 15px; width: 145px; height: 37px; border: 1.5px solid var(--teal);
    border-radius: 19px; color: var(--teal); font-size: 14px; text-align: center; line-height: 34px; }

  /* hero */
  .welcome-pill { left: 67px; top: 146px; width: 192px; height: 36px; border-radius: 10px;
    background: linear-gradient(90deg, #cdeef0, #e2f6cf); font-size: 13px; line-height: 36px; padding-left: 20px; color: var(--ink); }
  .hero-title { left: 72px; top: 188px; font-family: "Bree Serif", serif; font-size: 48px;
    line-height: 59px; color: var(--ink); white-space: nowrap; }
  .hero-title em { font-style: italic; }
  .hero-lead { left: 74px; top: 318px; width: 560px; font-size: 14.5px; line-height: 20px; color: var(--ink); }
  .feature { left: 74px; width: 500px; display: flex; gap: 17px; font-size: 11.5px; line-height: 14.2px; color: var(--ink); }
  .feature svg { flex: none; margin-top: -3px; }

  /* stake card */
  .stake-card { left: 701px; top: 113px; width: 385px; height: 466px; border-radius: 20px;
    background: rgba(255,255,255,.45); border: 1px solid rgba(255,255,255,.9); box-shadow: 0 10px 30px rgba(90,160,150,.08); }
  .card-title { left: 734px; top: 139px; font-family: "Bree Serif", serif; font-size: 25px; color: var(--ink); }
  .card-apy { left: 734px; top: 175px; font-size: 11.5px; color: #7fa49a; }
  .tabs { left: 734px; top: 204px; width: 319px; height: 46px; border-radius: 23px; background: rgba(245,247,246,.85); }
  .tab { top: 211px; width: 102px; height: 32px; line-height: 32px; text-align: center; font-size: 12px; color: #6c7874; }
  .tab.is-active { border: 1.5px solid var(--teal); border-radius: 16px; color: var(--teal); background: var(--white); line-height: 29px; }
  .field-label { font-size: 10px; color: var(--muted); }
  .amount-box { left: 734px; width: 319px; height: 48px; border-radius: 10px;
    background: rgba(255,255,255,.55); border: 1px solid rgba(255,255,255,.95); }
  .token-chip { left: 741px; height: 34px; border-radius: 8px; background: var(--white);
    display: flex; align-items: center; gap: 10px; padding-left: 7px; font-size: 12px; color: var(--ink); }
  .token-icon { width: 19px; height: 19px; border-radius: 50%; background: var(--token); }
  .amount { right: 161px; font-size: 26px; color: #98a4a2; }
  .quick-link { top: 347px; font-size: 10px; color: var(--muted); text-decoration: underline; }
  .connect-btn { left: 734px; top: 497px; width: 319px; height: 51px; border-radius: 26px;
    background: linear-gradient(90deg, #1ec8de, #8fe6a4 60%, #cdf27a);
    color: var(--white); font-size: 16px; text-align: center; line-height: 51px;
    box-shadow: 0 8px 16px rgba(90,200,190,.25); }
</style>
</head>
<body>
  <header class="site-header">
    <div class="abs brand"><span class="brand-dot"></span>Borvel Stake</div>
    <nav>
      <a class="abs nav-link is-active" style="left:623px;width:77px">Home</a>
      <a class="abs nav-link" style="left:722px;width:80px">Validators</a>
      <a class="abs nav-link" style="left:830px;width:60px">Docs</a>
    </nav>
    <div class="abs wallet-select">Select Wallet</div>
  </header>

  <main>
    <div class="abs welcome-pill">Welcome to Borvel Stake</div>
    <h1 class="abs hero-title">Your Gateway to<br><em>Liquid Staking</em> on Marevo</h1>
    <p class="abs hero-lead">Discover the power of liquid staking with Borvel Stake Pool, offering non-custodial staking services for MRV holders.</p>

    <div class="abs feature" style="top:404px">
      <svg width="18" height="18" viewBox="0 0 18 18"><circle cx="9" cy="9" r="8" fill="none" stroke="var(--check)" stroke-width="1.2"/><path d="M5.5 9.2l2.4 2.3 4.5-4.7" fill="none" stroke="var(--check)" stroke-width="1.3" stroke-linecap="round" stroke-linejoin="round"/></svg>
      <p>Borvel Stake Pool offers non-custodial staking. Stake your MRV to receive a liquid staking token, borvelMRV, that you can use in Defi on Marevo.</p>
    </div>
    <div class="abs feature" style="top:453px">
      <svg width="18" height="18" viewBox="0 0 18 18"><circle cx="9" cy="9" r="8" fill="none" stroke="var(--check)" stroke-width="1.2"/><path d="M5.5 9.2l2.4 2.3 4.5-4.7" fill="none" stroke="var(--check)" stroke-width="1.3" stroke-linecap="round" stroke-linejoin="round"/></svg>
      <p>Let us take care of managing your stake across the best validators on Marevo, and your staking rewards will be automatically compounded each epoch. The value of borvelMRV relative to MRV will increase every epoch.</p>
    </div>
    <div class="abs feature" style="top:517px">
      <svg width="18" height="18" viewBox="0 0 18 18"><circle cx="9" cy="9" r="8" fill="none" stroke="var(--check)" stroke-width="1.2"/><path d="M5.5 9.2l2.4 2.3 4.5-4.7" fill="none" stroke="var(--check)" stroke-width="1.3" stroke-linecap="round" stroke-linejoin="round"/></svg>
      <p>It is important for us you feel safe when staking with Borvel! Borvel Stake Pool is based on the Marevo Foundation stake pool program that has been audited 9 times.</p>
    </div>

    <section class="abs stake-card" aria-label="Staking panel"></section>
    <h2 class="abs card-title">Borvel Insight</h2>
    <p class="abs card-apy">Current APY: 8.03% across 60 validators</p>

    <div class="abs tabs"></div>
    <div class="abs tab is-active" style="left:740px">Stake</div>
    <div class="abs tab" style="left:843px">Unstake</div>
    <div class="abs tab" style="left:945px">Referral</div>

    <span class="abs field-label" style="left:734px;top:281px">Staking from</span>
    <span class="abs field-label" style="right:147px;top:281px">Balance: 0 MRV</span>
    <div class="abs amount-box" style="top:296px"></div>
    <div class="abs token-chip" style="top:303px;width:91px"><span class="token-icon"></span>MRV
      <svg width="10" height="10" viewBox="0 0 10 10"><path d="M2 3.5l3 3 3-3" fill="none" stroke="var(--ink)" stroke-width="1.3" stroke-linecap="round"/></svg></div>
    <span class="abs amount" style="top:302px">0.0</span>
    <a class="abs quick-link" style="left:987px">Max</a>
    <a class="abs quick-link" style="left:1021px">Half</a>

    <span class="abs field-label" style="left:734px;top:389px">Receives to</span>
    <span class="abs field-label" style="right:147px;top:389px">1 borvelMRV ~ 1.01714 MRV</span>
    <div class="abs amount-box" style="top:403px"></div>
    <div class="abs token-chip" style="top:410px;width:101px"><span class="token-icon"></span>borvelMRV</div>
    <span class="abs amount" style="top:409px">0.0</span>
    <span class="abs field-label" style="left:734px;top:454px">Balance: borvelMRV</span>

    <div class="abs connect-btn">Connect Wallet</div>
  </main>
</body>
</html>
```